Unique and original Business Card for Financial Services Business

I have moved premises and need to change the detail on my business card so thought now is a good time for a re-design. Looking for something professional and modern with colours to fit in with out logo. Like the idea of foil or embossing if that works but not a must have but I do want something that stands out and that I could not design myself.

Once business card is designed I will also be looking to get letterhead and flyers done but want the business card concept in place first.

The majority of designs I am receiving are generic and template based. I am looking for something unique and original. We have some great design elements in our logo, think outside the box and show me something that stands out from the crowd.

Target Market(s)

Business Professionals

Industry/Entity Type

Finance

Contact Information for Business Card

Name: Delia Norwood Phone 0473 958 162 Address PO Box 8617 Mossvale NSW 2389 Email info@steadyharbourfinancialservices.com.au website www.steadyharbourfinancialservices.com.au

Font styles to use
Other font styles liked:
• Ralway

Requirements
Should not have
• No black backgrounds please

```html
<!DOCTYPE html>
<html lang="en">
<head>
<meta charset="utf-8">
<title>Steady Harbour Financial Services – Business Card</title>
<link rel="stylesheet" href="https://fonts.googleapis.com/css2?family=Lexend:wght@300;400;500;700&display=swap">
<style>
  :root {
    --backdrop: #8f9090;
    --card-white: #ececee;
    --teal-deep: #0b5f6e;
    --teal-card: #007d8f;
    --teal-raised: #0aa3b4;
    --ink: #1d1d1f;
    --icon-glyph: #ffffff;
  }
  * { box-sizing: border-box; margin: 0; padding: 0; }
  html, body {
    width: 1200px;
    height: 1200px;
    overflow: hidden;
    background: var(--backdrop);
    font-family: "Lexend", sans-serif;
  }
  .canvas {
    position: relative;
    width: 1200px;
    height: 1200px;
  }
  .card {
    position: absolute;
    left: 233px;
    width: 748px;
    height: 416px;
  }
  .card--front {
    top: 101px;
    background: var(--card-white);
    text-align: center;
    color: var(--ink);
  }
  .card--back {
    top: 668px;
    background: var(--teal-card);
  }
  .brand-square {
    position: absolute;
    left: 50%;
    transform: translateX(-50%);
  }
  .card--front .brand-square {
    top: 40px;
    width: 58px;
    height: 58px;
    background: var(--teal-deep);
  }
  .card--back .brand-square {
    top: 100px;
    width: 128px;
    height: 128px;
    background: var(--teal-raised);
  }
  .brand {
    position: absolute;
    left: 0;
    right: 0;
    text-align: center;
    font-weight: 500;
    text-transform: uppercase;
  }
  .brand--front {
    top: 104px;
    color: var(--teal-deep);
  }
  .brand__name {
    display: block;
    letter-spacing: -0.5px;
  }
  .brand__tagline {
    display: block;
    text-transform: none;
  }
  .brand--front .brand__name { font-size: 30px; line-height: 32px; }
  .brand--front .brand__tagline { font-size: 15px; line-height: 18px; letter-spacing: 4.5px; }
  .person {
    position: absolute;
    top: 166px;
    left: 0;
    right: 0;
  }
  .person__name {
    font-size: 26px;
    font-weight: 700;
    color: var(--teal-deep);
    line-height: 32px;
  }
  .person__role {
    font-size: 18px;
    font-weight: 300;
    line-height: 24px;
  }
  .contact-icons {
    position: absolute;
    top: 241px;
    left: 0;
    right: 0;
    display: flex;
    justify-content: center;
    gap: 6px;
  }
  .contact-icons svg { width: 23px; height: 23px; display: block; }
  .contact-list {
    position: absolute;
    top: 277px;
    left: 0;
    right: 0;
    list-style: none;
    font-size: 19px;
    font-weight: 300;
    line-height: 25.5px;
  }
  .brand--back {
    top: 245px;
    color: var(--teal-raised);
    font-weight: 400;
  }
  .brand--back .brand__name { font-size: 54px; line-height: 56px; }
  .brand--back .brand__tagline { font-size: 27px; line-height: 34px; letter-spacing: 16px; }
</style>
</head>
<body>
<main class="canvas">

  <section class="card card--front" aria-label="Business card front">
    <div class="brand-square" aria-hidden="true"></div>
    <div class="brand brand--front">
      <span class="brand__name">Steady Harbour</span>
      <span class="brand__tagline">Financial Services</span>
    </div>

    <div class="person">
      <p class="person__name">Delia Norwood</p>
      <p class="person__role">Owner</p>
    </div>

    <div class="contact-icons">
      <svg viewBox="0 0 24 24" aria-label="Phone">
        <circle cx="12" cy="12" r="12" fill="var(--teal-deep)"/>
        <path d="M8.2 6.5l1.8-.4 1.2 3-1.3 1a7 7 0 0 0 3.9 3.9l1-1.3 3 1.2-.4 1.8c-5 .6-9.8-4.2-9.2-9.2z" fill="var(--icon-glyph)"/>
      </svg>
      <svg viewBox="0 0 24 24" aria-label="Address">
        <circle cx="12" cy="12" r="12" fill="var(--teal-deep)"/>
        <path d="M12 5a4.6 4.6 0 0 0-4.6 4.6C7.4 13 12 19 12 19s4.6-6 4.6-9.4A4.6 4.6 0 0 0 12 5z" fill="var(--icon-glyph)"/>
        <circle cx="12" cy="9.6" r="1.8" fill="var(--teal-deep)"/>
      </svg>
      <svg viewBox="0 0 24 24" aria-label="Email">
        <circle cx="12" cy="12" r="12" fill="var(--teal-deep)"/>
        <rect x="6" y="8" width="12" height="8.5" rx="1.2" fill="var(--icon-glyph)"/>
        <path d="M6.5 8.6L12 12.8l5.5-4.2" fill="none" stroke="var(--teal-deep)" stroke-width="1.2"/>
      </svg>
      <svg viewBox="0 0 24 24" aria-label="Website">
        <circle cx="12" cy="12" r="12" fill="var(--teal-deep)"/>
        <g fill="none" stroke="var(--icon-glyph)" stroke-width="1.2">
          <circle cx="12" cy="12" r="6"/>
          <ellipse cx="12" cy="12" rx="2.6" ry="6"/>
          <path d="M6 12h12M7 9h10M7 15h10"/>
        </g>
      </svg>
    </div>

    <ul class="contact-list">
      <li>0473 958 162</li>
      <li>PO Box 8617 Mossvale NSW 2389</li>
      <li>info@steadyharbourfinancialservices.com.au</li>
      <li>www.steadyharbourfinancialservices.com.au</li>
    </ul>
  </section>

  <section class="card card--back" aria-label="Business card back">
    <div class="brand-square" aria-hidden="true"></div>
    <div class="brand brand--back">
      <span class="brand__name">Steady Harbour</span>
      <span class="brand__tagline">Financial Services</span>
    </div>
  </section>

</main>
</body>
</html>
```